Best in class cloud software provider for retailers needs a new business card design to reflect prod

We are a software company based out of Chicago selling into retailers. We have a new website and marketing collateral that support our new product designs. We are obsessed with simplicity, ease of use, and having a really powerful product set. We have two products as noted on our website - www.plumvector.example - one is a retail task management product and the other is a Help Ticketing product.

At PlumVector we are passionate about creating the best Retail Task Management system in the industry. We bring more than 20 years of retail operations, Workforce Management and Retail Task experience and have a set of web and mobile software features that no one else has. PlumVector enables you to plan and distribute work throughout your organization and ensure it gets done.

We need a new business card design that reflects our new branding, message and approach.

I've attached a few documents that help support what we are building and how our colors look.

There may be additional future work if this goes well.

Thanks,
Brian

President

Target Market(s)

We sell into retailers and are a software company

Industry/Entity Type

Software

Contact Information for Business Card

The card must have

Name
title
address
tele
email
PlumVector logo (someplace)

So for example

It would have for me

Brian Okafor
President
47 North Garnet Ave. Suite 310
Chicago, IL 60618
3127814063
bokafor@plumvector.example

Requirements
Must have
• We need to cards for 5 different people - same design different names etc
Nice to have
• should reflect our colors and product and website - be creative - ease of use, simplicity, and power is what the product is about - but we are very forward PlumVector and hear all the time that our product is gorgeous. The font should be consistent with our website, and marketing one pager included
Should not have
• Strange or unfamiliar colors or fonts...

```html
<!DOCTYPE html>
<html lang="en">
<head>
<meta charset="utf-8">
<title>PlumVector Business Card</title>
<link href="https://fonts.googleapis.com/css2?family=Open+Sans:wght@400;600;700&display=swap" rel="stylesheet">
<style>
  :root {
    --brand-blue: #1f93c0;
    --brand-blue-light: #35b0d6;
    --brand-blue-deep: #1779a3;
    --card-white: #f4f5f5;
    --ink-grey: #4a4f53;
    --page-bg: #e6e8ea;
    --white: #ffffff;
  }
  * { margin: 0; padding: 0; box-sizing: border-box; }
  html, body {
    width: 1200px; height: 780px; overflow: hidden;
    background: var(--page-bg);
    font-family: "Open Sans", Arial, sans-serif;
  }
  .canvas {
    position: relative; width: 1200px; height: 780px;
    display: flex; align-items: center; justify-content: center; gap: 50px;
  }
  .card {
    width: 520px; height: 297px; position: relative; overflow: hidden;
    box-shadow: 0 6px 18px rgba(0,0,0,0.18);
  }

  /* Front */
  .card-front { background: var(--card-white); display: flex; flex-direction: column; }
  .front-logo-area {
    height: 112px; display: flex; align-items: center; padding-left: 48px;
  }
  .wordmark {
    font-weight: 700; font-size: 58px; color: var(--brand-blue);
    letter-spacing: -2px; line-height: 1;
  }
  .contact-band {
    height: 133px; display: flex; align-items: center; padding: 0 36px 0 48px;
    background: linear-gradient(90deg, var(--brand-blue) 0%, var(--brand-blue-light) 70%, var(--brand-blue) 100%);
    color: var(--white);
  }
  .person { width: 170px; text-align: right; padding-right: 22px; }
  .person-name { font-weight: 700; font-size: 22px; line-height: 1.15; }
  .person-title { font-weight: 400; font-size: 14px; }
  .band-divider { width: 1px; height: 78px; background: rgba(255,255,255,0.85); }
  .contact-list { list-style: none; padding-left: 20px; }
  .contact-list li {
    display: flex; align-items: center; gap: 8px;
    font-size: 13.5px; line-height: 24px;
  }
  .contact-icon {
    width: 16px; height: 16px; background: var(--white); border-radius: 2px;
    display: inline-flex; align-items: center; justify-content: center; flex: none;
  }
  .address-strip {
    flex: 1; display: flex; align-items: center; justify-content: center;
    font-size: 15px; color: var(--ink-grey);
  }

  /* Back */
  .card-back {
    background: radial-gradient(ellipse at 50% 45%, var(--brand-blue-light) 0%, var(--brand-blue) 55%, var(--brand-blue-deep) 100%);
    display: flex; align-items: center; justify-content: center;
  }
  .card-back .wordmark { color: var(--white); font-size: 56px; }
</style>
</head>
<body>
<main class="canvas">
  <section class="card card-front" aria-label="Business card front">
    <div class="front-logo-area">
      <span class="wordmark">PlumVector</span>
    </div>
    <div class="contact-band">
      <div class="person">
        <div class="person-name">Brian Okafor</div>
        <div class="person-title">President</div>
      </div>
      <div class="band-divider"></div>
      <ul class="contact-list">
        <li>
          <span class="contact-icon">
            <svg width="11" height="11" viewBox="0 0 24 24"><path fill="#1f93c0" d="M6.6 10.8a15.1 15.1 0 0 0 6.6 6.6l2.2-2.2a1 1 0 0 1 1-.25 11.4 11.4 0 0 0 3.6.57 1 1 0 0 1 1 1V20a1 1 0 0 1-1 1A17 17 0 0 1 3 4a1 1 0 0 1 1-1h3.5a1 1 0 0 1 1 1c0 1.25.2 2.45.57 3.6a1 1 0 0 1-.25 1z"/></svg>
          </span>3127814063
        </li>
        <li>
          <span class="contact-icon">
            <svg width="12" height="10" viewBox="0 0 24 18"><rect x="1" y="1" width="22" height="16" fill="none" stroke="#1f93c0" stroke-width="2.4"/><path d="M1 1l11 9 11-9" fill="none" stroke="#1f93c0" stroke-width="2.4"/></svg>
          </span>bokafor@plumvector.example
        </li>
        <li>
          <span class="contact-icon">
            <svg width="12" height="12" viewBox="0 0 24 24" fill="none" stroke="#1f93c0" stroke-width="2"><circle cx="12" cy="12" r="10"/><ellipse cx="12" cy="12" rx="4.5" ry="10"/><path d="M2 12h20"/></svg>
          </span>www.plumvector.example
        </li>
      </ul>
    </div>
    <div class="address-strip">47 North Garnet Ave. Suite 310 Chicago, IL 60618</div>
  </section>

  <section class="card card-back" aria-label="Business card back">
    <span class="wordmark">PlumVector</span>
  </section>
</main>
</body>
</html>
```